High Tech Software Startup needs Letterhead Design

We need a letterhead for a startup company base in Brazil. The letterhead should combine with our logo attached here.
We are a team of professionals in Java for web and mobile with iOS and android development.
We are looking for a modern and futuristc design.

Target Market(s)

CIO, IT managers of mid to big size companies

Industry/Entity Type

It Company

```html
<!DOCTYPE html>
<html lang="en">
<head>
<meta charset="utf-8">
<title>VOLTRA Letterhead</title>
<link href="https://fonts.googleapis.com/css2?family=Open+Sans:wght@400;600;700;800&family=Allura&display=swap" rel="stylesheet">
<style>
  :root {
    --backdrop: #e9ebee;
    --paper: #ffffff;
    --navy: #1b2d5c;
    --blue: #1f8fd0;
    --cyan: #1aa9e0;
    --deep: #22306e;
    --ink: #2a2d33;
    --muted: #4a4e57;
    --streak: #eef0f3;
  }
  * { box-sizing: border-box; margin: 0; padding: 0; }
  html, body { width: 1200px; height: 1024px; overflow: hidden; }
  body {
    background: var(--backdrop);
    font-family: "Open Sans", Arial, sans-serif;
    color: var(--ink);
    position: relative;
  }
  .letterhead {
    position: absolute;
    left: 253px; top: 22px;
    width: 694px; height: 980px;
    background: var(--paper);
    box-shadow: 0 4px 18px rgba(0,0,0,.18);
    overflow: hidden;
  }
  .streaks { position: absolute; inset: 0; width: 100%; height: 100%; }
  .brand {
    position: absolute; left: 52px; top: 58px;
    display: flex; align-items: center; gap: 12px;
  }
  .brand-square { width: 34px; height: 34px; background: var(--blue); }
  .brand-name {
    font-weight: 800; font-size: 46px; letter-spacing: 1px;
    color: var(--navy); line-height: 1;
  }
  .divider {
    position: absolute; left: 468px; top: 88px; width: 20px; height: 62px;
  }
  .contact {
    position: absolute; left: 500px; top: 100px;
    list-style: none; font-size: 11px; color: var(--navy); line-height: 1.35;
  }
  .contact li { display: flex; align-items: center; gap: 5px; }
  .contact svg { width: 9px; height: 9px; fill: var(--blue); flex: none; }
  .letter-body {
    position: absolute; left: 52px; top: 182px; width: 590px;
    font-size: 11px; line-height: 1.5; color: var(--muted);
  }
  .salutation { font-weight: 700; font-size: 13px; color: var(--ink); margin-bottom: 12px; }
  .letter-body p { margin-bottom: 10px; }
  .sign-off { margin-top: 18px; }
  .signature { font-family: "Allura", cursive; font-size: 30px; color: var(--navy); line-height: 1; }
  .role { font-size: 11px; color: var(--muted); }
  .address-band {
    position: absolute; left: 0; right: 0; bottom: 0; height: 56px;
    background: linear-gradient(90deg, var(--cyan) 0%, #1b86c9 45%, var(--deep) 100%);
    color: #ffffff; font-size: 14px;
    display: flex; align-items: center; padding-left: 96px;
  }
</style>
</head>
<body>
  <main class="letterhead">
    <svg class="streaks" viewBox="0 0 694 980" preserveAspectRatio="none" aria-hidden="true">
      <polygon points="0,150 694,60 694,130 0,260" fill="var(--streak)"/>
      <polygon points="0,480 694,260 694,300 0,560" fill="var(--streak)" opacity=".8"/>
      <polygon points="0,640 694,420 694,450 0,700" fill="var(--streak)" opacity=".7"/>
      <polygon points="120,924 694,700 694,760 300,924" fill="var(--streak)" opacity=".7"/>
    </svg>

    <header class="brand">
      <span class="brand-square"></span>
      <span class="brand-name">VOLTRA</span>
    </header>

    <svg class="divider" viewBox="0 0 20 62" aria-hidden="true">
      <line x1="18" y1="0" x2="2" y2="62" stroke="var(--blue)" stroke-width="1.4"/>
    </svg>

    <ul class="contact">
      <li><svg viewBox="0 0 10 10"><path d="M2 0h2l1 3-1.5 1a6 6 0 0 0 2.5 2.5L7 5l3 1v2a2 2 0 0 1-2 2A8 8 0 0 1 0 2a2 2 0 0 1 2-2z"/></svg>000.000.0000</li>
      <li><svg viewBox="0 0 10 10"><rect x="1" y="0" width="8" height="10" rx="1"/></svg>000.000.0000</li>
      <li><svg viewBox="0 0 10 10"><path d="M0 2h10v6H0z"/></svg>name@domainname.com</li>
      <li><svg viewBox="0 0 10 10"><circle cx="5" cy="5" r="5"/></svg>www.wesitename.com</li>
    </ul>

    <section class="letter-body">
      <p class="salutation">Lorem Ipsum,</p>
      <p>Duis sit amet dolor sit amet dolor tempor iaculis ac nec ante. Proin nunc diam, egestas eu semper a, fermentum ac leo. Fusce sit amet tempor elit. Mauris auctor interdum massa vitae cursus. Ut adipiscing pellentesque nunc, eget tincidunt magna imperdiet non. Curabitur eleifend elementum nisl eget iaculis. Suspendisse scelerisque ligula a nunc faucibus sit amet elementum dolor dictum.</p>
      <p>Praesent condimentum mi at ultrices fermentum, ipsum lectus consequat mauris, ut vulputate nibh erat id eros. Vivamus ornare mattis libero at dictum. Praesent sodales metus sed nulla laoreet mollis. Curabitur non turpis in orci dignissim gravida. Aliquam tristique mauris a nibh vestibulum sagittis.</p>
      <p>Duis porta semper nibh, tincidunt aliquam metus euismod eget. Morbi varius varius pellentesque. Donec aliquam vulputate tortor non hendrerit. Suspendisse at ipsum ante, interdum porttitor ligula. Curabitur eu molestie sapien. Sed magna purus, faucibus quis pulvinar nec, commodo vel justo. Nam faucibus ornare varius. Vivamus sit amet felis vitae justo scelerisque malesuada. Etiam venenatis vehicula magna, a eleifend lorem ornare nec. Maecenas eu nisl vel nunc aliquet malesuada vel in lacus.</p>
      <p>Morbi et odio eu ante pharetra iaculis vitae eget arcu. Maecenas gravida, dui vel ultricies aliquet, dui arcu luctus ante, non dignissim ipsum tortor vel orci, um fringilla mi. Mauris porta feugiat nibh et fermentum. Donec scelerisque consequat lacinia.</p>
      <p>Curabitur ac diam ut quam ultrices laoreet at ut tellus. Maecenas vitae urna in lorem condimentum sollicitudin eget vel lacus. Ut nisi turpis, tristique ullamcorper laoreet nec, gravida nec est. Donec elementum malesuada volutpat. In ac arcu quis augue vehicula fringilla.</p>
      <p>Pellentesque habitant morbi tristique senectus et netus et malesuada fames ac turpis egestas. In posuere felis nec tortor. Pellentesque faucibus. Ut accumsan ultricies elit. Maecenas at justo id velit placerat molestie.</p>
      <div class="sign-off">
        <div class="signature">Yours Name</div>
        <div class="role">Company Director</div>
      </div>
    </section>

    <footer class="address-band">Your Address goes here, Str name, City, Zip Code, Country Name</footer>
  </main>
</body>
</html>
```